Wedding Day Custom Wine Label - Tasmanian (Tamar Valley) wine

I am looking for a custom design that will be put on a wine label to commemorate a very good friend's wedding day.

We will need to be able to take the design and print it on to sticker labels that we can put on to wine bottles.

The bride and groom have asked for a simplistic label design (see example image attached). We need two labels. One for "Pinot Noir" wine and the other for "Chardonnay" wine. We would like the label to say:

The Hartwell's
Pinot Noir
2023
Tamar Valley

and for for the other wine variety:

The Hartwell's
Chardonnay
2023
Tamar Valley

smaller text below to say:

13.5% ALC/VOL 750ML
MEGAN & LIAM - 31.10.2024

I am happy to consider other variations - the bride & groom would prefer something minimalistic. Elegant and classy.

Target Market(s)

the bride & groom

Requirements
Must have
• Wedding date (31.10.2024). Wine type (Pinot Noir or Chardonnay).
Should not have
• images not essential

```html
<!DOCTYPE html>
<html lang="en">
<head>
<meta charset="utf-8">
<title>The Hartwell's — Pinot Noir 2023 Label</title>
<link href="https://fonts.googleapis.com/css2?family=Courier+Prime:wght@400;700&display=swap" rel="stylesheet">
<style>
  :root {
    --backdrop: #e4e3e0;
    --paper: #efeeeb;
    --ink: #1e1c1c;
    --wine-red: #8a1a1e;
    --edge: #d9d7d3;
  }
  html, body {
    margin: 0;
    width: 1200px;
    height: 1200px;
    overflow: hidden;
    background: var(--backdrop);
  }
  .canvas {
    width: 1200px;
    height: 1200px;
    display: flex;
    align-items: center;
    justify-content: center;
  }
  .label {
    width: 760px;
    height: 1000px;
    background: var(--paper);
    border: 1px solid var(--edge);
    box-sizing: border-box;
    display: flex;
    flex-direction: column;
    align-items: center;
    text-align: center;
    padding: 70px 40px 0;
    box-shadow: 0 6px 24px rgba(0,0,0,0.08);
  }
  .label__brand {
    font-family: "Courier Prime", "Courier New", monospace;
    font-weight: 700;
    color: var(--ink);
    font-size: 104px;
    line-height: 1.05;
    letter-spacing: 0;
    margin: 0;
    text-transform: uppercase;
    white-space: nowrap;
  }
  .label__variety {
    font-family: "Courier Prime", "Courier New", monospace;
    font-weight: 700;
    color: var(--wine-red);
    font-size: 54px;
    letter-spacing: 6px;
    margin: 200px 0 0;
    line-height: 1.1;
  }
  .label__vintage {
    font-family: "Courier Prime", "Courier New", monospace;
    font-weight: 700;
    color: var(--wine-red);
    font-size: 48px;
    letter-spacing: 6px;
    margin: 4px 0 0;
    line-height: 1.1;
  }
  .label__region {
    font-family: "Courier Prime", "Courier New", monospace;
    font-weight: 700;
    color: var(--ink);
    font-size: 36px;
    letter-spacing: 7px;
    margin: 34px 0 0;
  }
  .label__details {
    margin-top: auto;
    margin-bottom: 56px;
    font-family: "Courier Prime", "Courier New", monospace;
    font-weight: 700;
    color: var(--ink);
    font-size: 22px;
    line-height: 1.3;
  }
  .label__details p { margin: 0; }
</style>
</head>
<body>
  <main class="canvas">
    <article class="label">
      <h1 class="label__brand">The<br>Hartwell's</h1>
      <p class="label__variety">PINOT NOIR</p>
      <p class="label__vintage">2023</p>
      <p class="label__region">TAMAR VALLEY</p>
      <div class="label__details">
        <p>13.5% ALC/VOL 750ML</p>
        <p>MEGAN &amp; LIAM - 31.10.2024</p>
      </div>
    </article>
  </main>
</body>
</html>
```